Goldschmiede sucht Flyer mit GUtschein abriss
Zielgruppe
ICh bin ein Goldschmied in Saarbrücken Trier und Mainz und mache jegliche Dienstleistungen eines Goldschmiedes.Es sollen noch mit ein paar passenden Fotos gearbeitet werden.
Aufgabenstellung
Ich suche einen Flyer für meine Goldschmiede vorhandene Punkte sollen sein.
Reparaturen aller Art , Ringweitenänderung, Löten , Polieren / Aufarbeiten , Neuanfertigung nach Wunsch ,Rhodienieren , Gravieren , usw.
Der Flyer soll am unteren Rand die Möglichkeit haben, abgeschnitten zu werden dort soll ein Gutschein entstehen zb. mit 20 % Rabatt.
( der Abriss soll nummeriert werden damit niemand kopiert oder mehrfach abgibt )
Auf der Internetseite können Sie sich meine Firmenfarben ansehen in diesen Farben soll auch das Flyer-Design sein.
Bei der Adresse sollen alle drei Filialen angegeben werden.

```html
<!DOCTYPE html>
<html lang="de">
<head>
<meta charset="utf-8">
<title>Goldschmiede Flyer</title>
<link rel="stylesheet" href="https://fonts.googleapis.com/css2?family=Jost:wght@300;400;500;700&display=swap">
<style>
  :root {
    --page-bg: #dcdcdc;
    --charcoal: #4a4a4c;
    --charcoal-deep: #3f3f41;
    --gold: #b8a46a;
    --gold-text: #c9b37a;
    --gold-light: #e8dcb8;
    --sepia-dark: #6e6248;
    --muted: #6f6f70;
    --white: #ffffff;
  }
  * { box-sizing: border-box; margin: 0; padding: 0; }
  html, body {
    width: 1200px; height: 1200px; overflow: hidden;
    background: var(--page-bg);
    font-family: "Jost", "Futura", sans-serif;
  }
  .flyer {
    position: absolute; left: 210px; top: 48px;
    width: 780px; height: 1104px;
    background: var(--charcoal);
    overflow: hidden;
  }
  .brand {
    position: absolute; left: 0; right: 0; top: 70px;
    text-align: center; color: var(--gold-text);
  }
  .brand-name { font-size: 44px; font-weight: 400; letter-spacing: 1px; line-height: 1.1; }
  .brand-trade { font-size: 44px; font-weight: 400; letter-spacing: 1px; line-height: 1.1; }

  .photo-band {
    position: absolute; left: 0; top: 228px; width: 780px; height: 460px;
    background: var(--gold-light);
    border-top: 6px solid var(--gold);
    border-bottom: 6px solid var(--gold);
  }
  .photo-workbench {
    position: absolute; left: 0; top: 10px; width: 512px; height: 432px;
    background: linear-gradient(100deg, #f1e9d0 0%, #ddd0a8 45%, #8e7f5c 70%, #efe6ca 100%);
  }
  .photo-tools {
    position: absolute; left: 517px; top: 10px; width: 263px; height: 250px;
    background: linear-gradient(160deg, #d9cba3 0%, #7b6d4f 55%, #3e372a 100%);
  }
  .photo-engraving {
    position: absolute; left: 517px; top: 270px; width: 263px; height: 172px;
    background: linear-gradient(200deg, #cfc19a 0%, #8a7b58 50%, #4a4232 100%);
  }
  .services { position: absolute; left: 0; top: 36px; list-style: none; }
  .service {
    position: relative; height: 31px; width: 350px; margin-bottom: 20px;
    background: var(--charcoal);
    clip-path: polygon(0 0, 100% 0, calc(100% - 28px) 100%, 0 100%);
    color: var(--gold-text); font-size: 18px; font-weight: 400;
    line-height: 31px; padding-left: 40px;
  }
  .service.wide { width: 375px; }
  .service::before {
    content: ""; position: absolute; left: 20px; top: 10px;
    width: 5px; height: 9px;
    border-right: 2px solid var(--gold-text); border-bottom: 2px solid var(--gold-text);
    transform: rotate(40deg);
  }

  .contact-heading, .hours-heading {
    position: absolute; left: 64px; color: var(--white);
    font-size: 22px; font-weight: 500; letter-spacing: 0.5px;
  }
  .contact-heading { top: 706px; }
  .hours-heading { top: 880px; }
  .branch { position: absolute; top: 752px; color: var(--gold-text); font-size: 15px; line-height: 20px; }
  .branch-city { font-weight: 700; font-size: 17px; margin-bottom: 6px; }
  .branch-sb { left: 64px; }
  .branch-tr { left: 325px; }
  .branch-mz { left: 563px; }
  .hours { position: absolute; left: 64px; top: 918px; color: var(--gold-text); font-size: 15px; line-height: 22px; }

  .photo-rings {
    position: absolute; left: 41px; top: 1001px; width: 142px; height: 84px;
    background: radial-gradient(ellipse at 50% 55%, #f4ecd2 0%, #c8b37a 45%, var(--charcoal) 75%);
  }
  .website {
    position: absolute; left: 0; width: 560px; top: 1056px;
    text-align: center; color: var(--gold-text); font-size: 15px;
  }
  .voucher { position: absolute; left: 0; top: 0; width: 780px; height: 1104px; }
  .voucher text { font-family: "Jost", "Futura", sans-serif; }
</style>
</head>
<body>
  <main class="flyer">
    <header class="brand">
      <div class="brand-name">Lena Hofmeister</div>
      <div class="brand-trade">Goldschmiede</div>
    </header>

    <section class="photo-band">
      <div class="photo-workbench" role="img" aria-label="Goldschmiedewerkbank mit Werkzeugen und Schmuckketten, sepiafarben"></div>
      <div class="photo-tools" role="img" aria-label="Polier- und Schleifaufsätze für die Schmuckbearbeitung"></div>
      <div class="photo-engraving" role="img" aria-label="Hände beim Gravieren eines Rings"></div>
      <ul class="services">
        <li class="service">Reparaturen aller Art</li>
        <li class="service">Ringweitenänderung</li>
        <li class="service">Löten</li>
        <li class="service">Polieren / Aufarbeiten</li>
        <li class="service wide">Neuanfertigung nach Wunsch</li>
        <li class="service">Rhodienieren</li>
        <li class="service">Gravieren</li>
        <li class="service">und vieles mehr</li>
      </ul>
    </section>

    <h2 class="contact-heading">SIE ERREICHEN UNS IN:</h2>
    <address class="branch branch-sb" style="font-style:normal">
      <div class="branch-city">Saarbrücken</div>
      Lindenallee 7<br>66111 Saarbrücken<br>Tel: 0681 - 12 345 678
    </address>
    <address class="branch branch-tr" style="font-style:normal">
      <div class="branch-city">Trier</div>
      Am Kornmarkt 4<br>54290 Trier<br>Tel: 0651 - 55 210 34
    </address>
    <address class="branch branch-mz" style="font-style:normal">
      <div class="branch-city">Mainz</div>
      Rheinufer 22<br>55116 Mainz<br>Tel: 06131 - 470 20 10
    </address>

    <h2 class="hours-heading">ÖFFNUNGSZEITEN:</h2>
    <p class="hours">Montag bis Freitag: 9:30 bis 18:00 Uhr<br>Samstag: 9:30 bis 14:00 Uhr</p>

    <div class="photo-rings" role="img" aria-label="Zwei goldene Eheringe"></div>
    <p class="website">www.hofmeister-gold.de</p>

    <svg class="voucher" viewBox="0 0 780 1104" aria-label="Gutschein zum Abtrennen">
      <polygon points="557,1104 780,1104 780,827" fill="var(--gold)"/>
      <g transform="translate(557,1104) rotate(-51.2)">
        <line x1="0" y1="0" x2="356" y2="0" stroke="var(--charcoal-deep)" stroke-width="1.5" stroke-dasharray="6 5"/>
        <text x="185" y="-10" text-anchor="middle" font-size="38" font-weight="300" fill="var(--muted)" letter-spacing="1">GUTSCHEIN</text>
        <text x="173" y="24" text-anchor="middle" font-size="14" font-weight="500" fill="var(--charcoal-deep)">AUF ALLE GOLDSCHMIEDEARBEITEN</text>
        <text x="166" y="56" text-anchor="middle" font-size="30" font-weight="700" fill="var(--white)">20% RABATT</text>
        <text x="160" y="82" text-anchor="middle" font-size="16" font-weight="400" fill="var(--charcoal-deep)">NR. 0011</text>
      </g>
    </svg>
  </main>
</body>
</html>
```